Lantern Business Cards

Need business cards for my employees at my restaurant.

Needs to include:
Our Logo
Lantern Bowls & Brews
Name: Nora Pettigrew
Title : Owner
Address: 487 Mirella Ave. Kestrel Lake, CO 80519
Web: www.lanternkestrel.com
Phone: 555-555-0147
Cell: 555-555-0192
Email: info@lanternkestrel.com

```html
<!DOCTYPE html>
<html lang="en">
<head>
<meta charset="utf-8">
<title>Lantern Bowls &amp; Brews – Business Cards</title>
<link href="https://fonts.googleapis.com/css2?family=Arimo:wght@700&family=Cabin:ital,wght@0,500;1,400&family=Open+Sans:ital,wght@1,400&display=swap" rel="stylesheet">
<style>
  :root {
    --red: #b71c2c;
    --red-deep: #7a0f1e;
    --black: #0b0b0b;
    --charcoal: #5a5a5a;
    --white: #ffffff;
    --ink: #151515;
    --page: #ffffff;
    --edge: #e6e6e6;
  }
  * { margin: 0; padding: 0; box-sizing: border-box; }
  html, body { width: 1200px; height: 1200px; overflow: hidden; background: var(--page); }
  .canvas { position: relative; width: 1200px; height: 1200px; }

  .card { position: absolute; width: 722px; height: 389px; overflow: hidden; }

  /* Front */
  .card-front {
    left: 246px; top: 164px;
    background: radial-gradient(ellipse 60% 55% at 50% 50%, var(--red-deep) 0%, #9a1626 50%, var(--red) 100%);
  }
  .front-brand {
    position: absolute; left: 0; right: 0; top: 164px;
    display: flex; align-items: center; justify-content: center; gap: 18px;
    font-family: "Cabin", sans-serif; font-weight: 500; font-size: 44px; color: var(--white);
    white-space: nowrap;
  }
  .front-brand .mark { width: 60px; height: 60px; border-radius: 50%; background: var(--white); flex: none; }

  /* Back */
  .card-back { left: 251px; top: 594px; background: var(--white); border: 1px solid var(--edge); border-bottom: 0; }
  .phones {
    position: absolute; left: 68px; top: 62px;
    font-family: "Arimo", sans-serif; font-weight: 700; font-size: 24px; color: var(--ink);
    display: flex; gap: 32px; white-space: nowrap;
  }
  .phones .label { color: var(--red); }

  .back-brand {
    position: absolute; left: 26px; top: 176px; display: flex; align-items: center; gap: 12px;
    font-family: "Cabin", sans-serif; font-weight: 500; font-size: 23px; color: var(--red);
    white-space: nowrap;
  }
  .back-brand .mark { width: 44px; height: 44px; border-radius: 50%; background: var(--red); flex: none; }

  .name-band { position: absolute; left: 0; top: 142px; width: 722px; height: 116px; }
  .person {
    position: absolute; left: 410px; width: 260px; top: 170px; text-align: center; color: var(--white);
    font-family: "Cabin", sans-serif;
  }
  .person .full-name { display: block; font-size: 36px; font-weight: 500; line-height: 1; white-space: nowrap; }
  .person .role { display: block; font-size: 21px; font-style: italic; margin-top: 2px; }

  .contact-band {
    position: absolute; left: 0; top: 257px; width: 722px; height: 132px;
    background: radial-gradient(ellipse 45% 80% at 40% 0%, var(--charcoal) 0%, #1c1c1c 65%, var(--black) 100%);
    font-family: "Open Sans", sans-serif; font-style: italic; color: var(--white); font-size: 17.5px;
  }
  .contact { position: absolute; display: flex; align-items: center; gap: 18px; white-space: nowrap; }
  .contact-email { left: 66px; top: 36px; }
  .contact-web { left: 404px; top: 24px; gap: 14px; }
  .address { position: absolute; left: 0; right: 0; top: 85px; text-align: center; white-space: nowrap; }
</style>
</head>
<body>
<main class="canvas">

  <section class="card card-front" aria-label="Card front">
    <div class="front-brand"><span class="mark"></span><span>Lantern Bowls &amp; Brews</span></div>
  </section>

  <section class="card card-back" aria-label="Card back">
    <div class="phones">
      <span><span class="label">Phone NO.</span> 555-555-0147</span>
      <span><span class="label">Cell NO.</span> 555-555-0192</span>
    </div>

    <div class="back-brand"><span class="mark"></span><span>Lantern Bowls &amp; Brews</span></div>

    <svg class="name-band" viewBox="0 0 722 116" aria-hidden="true">
      <polygon points="386,0 722,0 722,116 271,116" fill="var(--red)"/>
    </svg>
    <div class="person">
      <span class="full-name">Nora Pettigrew</span>
      <span class="role">Owner</span>
    </div>

    <div class="contact-band">
      <div class="contact contact-email">
        <svg width="34" height="22" viewBox="0 0 34 22" aria-hidden="true">
          <rect x="0" y="0" width="34" height="22" fill="var(--red)"/>
          <polyline points="1,1 17,13 33,1" fill="none" stroke="var(--black)" stroke-width="2"/>
          <line x1="1" y1="21" x2="13" y2="10" stroke="var(--black)" stroke-width="2"/>
          <line x1="33" y1="21" x2="21" y2="10" stroke="var(--black)" stroke-width="2"/>
        </svg>
        <span>info@lanternkestrel.com</span>
      </div>
      <div class="contact contact-web">
        <svg width="30" height="30" viewBox="0 0 30 30" aria-hidden="true">
          <circle cx="15" cy="15" r="13" fill="none" stroke="var(--red)" stroke-width="3"/>
          <ellipse cx="15" cy="15" rx="5.5" ry="13" fill="none" stroke="var(--red)" stroke-width="2"/>
          <line x1="2" y1="15" x2="28" y2="15" stroke="var(--red)" stroke-width="2"/>
        </svg>
        <span>www.lanternkestrel.com</span>
      </div>
      <div class="address">487 Mirella Ave. Kestrel Lake, CO 80519</div>
    </div>
  </section>

</main>
</body>
</html>
```